Solo consultant in research/analytics/data science space needs new business card

I need a new business card to promote my solo business as creative problem solver and consultant. I work on business projects for sales and market research and analytics, customer/market insights, and data science. I provide clients data-informed insights and ideas to enhance their businesses. My initial tagline: 'Make your data work for YOU.'

People should hire me because of my diverse background. Because of my Ph.D. in Political Science I have a strong background in research and analytics, project design and management, and communications skills. With my experience as a marketing analyst, a volunteer on non-profit projects, and currently as research consultant I have worked on projects within various industries. I also have a taste for improvisation so I enjoy thinking creatively and appreciate design thinking.

As an introduction to my background: Clients might want to hire me for many types of projects. Clients might wish to understand who their best customers are and how to characterize them. Maybe clients want to know how their customers feel about a certain product or service. Clients might want to know more about their local market area and overall industry. Clients might want to know whether their marketing programs are effective or else what drives their sales revenue. Perhaps clients want to use their data to create something useful for themselves or their customers.

One client hired me to help them decide whether to expand their services to newer customers. I gathered and analyzed information about the local area – the characteristics of people living there as well as the client’s competitors – and described trends and implications. The client was very pleased with the results and submitted them to superiors for approval to move forward.

For another client – who was looking to purchase a house in a metropolitan area – I gathered population and school data about the area. With this, I created an interactive mapping tool so they could zoom in on neighborhoods and learn more about them before they selected a neighborhood to purchase a house. They were happy with the results of my work.

When I worked as a marketing analyst for a consulting firm, a Vice President of Marketing hired us to discover whether or not the company’s marketing programs (i.e. coupons and discounts) were effective. I analyzed their data and our team discovered their marketing was indeed effective. He was very happy and used this to justify their programs to the Finance department (who thought such programs lost revenue).

- Mark Dennis Hollow, Ph.D.

Target Market(s)

Future clients and employers. The most immediate target markets will be other service providers such as consulting companies, marketing firms and ad agencies. I will also use this for meeting with clients in various industries.

Industry/Entity Type

Consulting

Contact Information for Business Card

Since it is my first real business card as a solo practitioner, I want to make an excellent first impression. I want this useful in case someone hires me to work on projects or else hire me to work within a firm or company. The card should convey competence and some creativity while also being neither stuffy nor a data geek.

Colors

Designer to choose colors to be used in the design.

Requirements
Nice to have
• Attached are the starting efforts at the card to add some color. It will be nice to use my name and descriptors on one side and tagline on the other. If anyone has better ideas, I will love to see them!

```html
<!DOCTYPE html>
<html lang="en">
<head>
<meta charset="utf-8">
<title>Mark Dennis Hollow, Ph.D. – Business Card</title>
<link href="https://fonts.googleapis.com/css2?family=Roboto:wght@400;500;700&display=swap" rel="stylesheet">
<style>
  :root {
    --accent: #e05e4a;
    --ink: #2d2d2d;
    --muted: #555555;
    --paper: #ffffff;
    --backdrop: #e4e4e4;
  }
  html, body {
    margin: 0;
    padding: 0;
    overflow: hidden;
  }
  body {
    width: 1125px;
    height: 1200px;
    position: relative;
    background: var(--backdrop);
    font-family: "Roboto", Arial, sans-serif;
  }
  .card {
    position: absolute;
    left: 171px;
    width: 826px;
    height: 472px;
    background: var(--paper);
    box-shadow: 0 1px 3px rgba(0,0,0,0.25);
    box-sizing: border-box;
  }
  .card--front {
    top: 106px;
    border-left: 17px solid var(--accent);
    border-right: 17px solid var(--ink);
  }
  .card--back {
    top: 640px;
  }
  .line {
    position: absolute;
    left: 0;
    right: 0;
    margin: 0;
    text-align: center;
    white-space: nowrap;
    line-height: 1.1;
  }
  .name {
    top: 112px;
    font-size: 47px;
    font-weight: 500;
    color: var(--accent);
  }
  .disciplines {
    top: 168px;
    font-size: 20px;
    font-weight: 500;
    color: var(--ink);
  }
  .role {
    top: 221px;
    font-size: 31px;
    font-weight: 500;
    color: var(--accent);
  }
  .location {
    top: 256px;
    font-size: 18px;
    color: var(--muted);
  }
  .contact {
    font-size: 19px;
    color: var(--muted);
    display: flex;
    justify-content: center;
    align-items: center;
    gap: 10px;
  }
  .contact--one { top: 305px; }
  .contact--two { top: 332px; }
  .contact-item {
    display: inline-flex;
    align-items: center;
    gap: 3px;
  }
  .icon {
    width: 17px;
    height: 17px;
    fill: var(--accent);
    flex: none;
  }
  .tagline {
    top: 172px;
    font-size: 53px;
    font-weight: 700;
    line-height: 64px;
    color: var(--ink);
  }
</style>
</head>
<body>

<section class="card card--front">
  <h1 class="line name">Mark Dennis Hollow, Ph.D.</h1>
  <p class="line disciplines">Research/Analytics-Customer Intelligence - Data Science</p>
  <p class="line role">Consultant</p>
  <p class="line location">Lisbon,PT</p>

  <p class="line contact contact--one">
    <span class="contact-item">
      <svg class="icon" viewBox="0 0 24 24" aria-hidden="true"><path d="M6.6 10.8c1.4 2.8 3.8 5.1 6.6 6.6l2.2-2.2c.3-.3.7-.4 1-.2 1.1.4 2.3.6 3.6.6.6 0 1 .4 1 1V20c0 .6-.4 1-1 1C10.6 21 3 13.4 3 4c0-.6.4-1 1-1h3.5c.6 0 1 .4 1 1 0 1.3.2 2.5.6 3.6.1.3 0 .7-.2 1l-2.3 2.2z"/></svg>
      +351 910 555 284
    </span>
    <span class="contact-item">
      <svg class="icon" viewBox="0 0 24 24" aria-hidden="true"><path d="M3 5h18v14H3z M3 5l9 7 9-7" fill="var(--accent)"/><path d="M4 6.5l8 6.2 8-6.2" fill="none" stroke="#fff" stroke-width="1.6"/></svg>
      mdhollow70@postbox.net
    </span>
  </p>

  <p class="line contact contact--two">
    <span class="contact-item">
      <svg class="icon" viewBox="0 0 24 24" aria-hidden="true"><circle cx="12" cy="12" r="9"/><path d="M3 12h18M12 3c3 3 3 15 0 18M12 3c-3 3-3 15 0 18" fill="none" stroke="#fff" stroke-width="1.4"/></svg>
      markdennishollow.com
    </span>
    <span class="contact-item">
      <svg class="icon" viewBox="0 0 24 24" aria-hidden="true"><circle cx="12" cy="12" r="8"/></svg>
      @MarkHollow70
    </span>
  </p>
</section>

<section class="card card--back">
  <p class="line tagline">Make your data<br>work for you.</p>
</section>

</body>
</html>
```